Professional Report Cover

We need a cover for CFO report (the document is about 20 pages, in case you decide to provide 3D mockup). The design must be professional. The main color has to be #299FC0, which can be incorporated with white, #375172, and #E3E7EE. See attached for content and logo.

```html
<!DOCTYPE html>
<html lang="en">
<head>
<meta charset="utf-8">
<title>The CFO Outlook – Report Cover</title>
<link rel="stylesheet" href="https://fonts.googleapis.com/css2?family=Playfair+Display:wght@400;600&family=Montserrat:wght@400;500;600&display=swap">
<style>
  :root {
    --brand-teal: #299FC0;
    --navy: #375172;
    --deep-navy: #1c2f5a;
    --mist: #E3E7EE;
    --white: #ffffff;
    --stage: #eef0f3;
  }
  * { margin: 0; padding: 0; box-sizing: border-box; }
  html, body { width: 1200px; height: 2460px; overflow: hidden; background: var(--stage); }
  .canvas {
    width: 1200px; height: 2460px;
    display: flex; align-items: center; justify-content: center;
  }
  .cover {
    position: relative;
    width: 960px; height: 1360px;
    background: linear-gradient(160deg, var(--deep-navy) 0%, var(--navy) 55%, #2a6f95 100%);
    overflow: hidden;
    color: var(--white);
    font-family: "Montserrat", sans-serif;
  }
  .brand {
    position: absolute; top: 70px; left: 0; right: 0;
    display: flex; align-items: center; justify-content: center; gap: 14px;
    font-weight: 600; font-size: 22px; letter-spacing: 3px; text-transform: uppercase;
    color: var(--white);
  }
  .brand-square { width: 26px; height: 26px; background: var(--white); }
  .title {
    position: absolute; top: 160px; left: 0; right: 0;
    text-align: center;
    font-family: "Playfair Display", serif; font-weight: 400;
    font-size: 124px; line-height: 1.0; letter-spacing: 2px;
    color: var(--mist);
  }
  .subtitle {
    position: absolute; top: 440px; left: 90px; right: 90px;
    text-align: center;
    font-size: 19px; line-height: 1.4; letter-spacing: 2px; text-transform: uppercase;
    color: var(--brand-teal); font-weight: 500;
  }
  .details {
    position: absolute; top: 540px; left: 90px; width: 460px;
    font-size: 18px; line-height: 1.7; color: var(--mist);
  }
  .details .lead { color: var(--brand-teal); font-weight: 600; }
  .growth-art { position: absolute; left: 0; top: 700px; width: 960px; height: 520px; }
  .author-band { position: absolute; left: 0; bottom: 0; width: 960px; height: 300px; }
  .author-name {
    position: absolute; left: 0; right: 0; bottom: 92px;
    text-align: center;
    font-size: 44px; font-weight: 500; letter-spacing: 6px;
    color: var(--navy);
    transform: rotate(-6deg);
  }
</style>
</head>
<body>
<main class="canvas">
  <section class="cover">
    <div class="brand"><span class="brand-square"></span>Meridian Ledger</div>
    <h1 class="title">THE CFO<br>OUTLOOK</h1>
    <p class="subtitle">Strategic Financial Perspectives<br>for Growth&#8209;Minded Leadership Teams</p>
    <div class="details">
      <p class="lead">Quarterly briefing on capital, risk and performance</p>
      <p>Prepared for the Executive Board</p>
      <p>Edition 2024 · Volume One</p>
    </div>
    <svg class="growth-art" viewBox="0 0 960 520" role="img" aria-label="Rising arrows illustration in teal and green tones symbolising growth">
      <defs>
        <linearGradient id="arrowTone" x1="0" y1="1" x2="1" y2="0">
          <stop offset="0" stop-color="#299FC0" stop-opacity="0.35"/>
          <stop offset="1" stop-color="#3fc7a8" stop-opacity="0.9"/>
        </linearGradient>
      </defs>
      <polygon points="260,520 720,40 960,40 960,520" fill="url(#arrowTone)"/>
    </svg>
    <svg class="author-band" viewBox="0 0 960 300" preserveAspectRatio="none">
      <polygon points="0,200 960,60 960,180 0,300" fill="var(--mist)"/>
      <polygon points="0,300 960,180 960,300" fill="var(--white)"/>
    </svg>
    <p class="author-name">AUTHOR NAME</p>
  </section>
</main>
</body>
</html>
```